Introduction of new dentist and new treatments

We want inform our Patients of our new dentist and new treatment methods. It is dealing about biologic dentistry and holistic dentistry. we are in switzerland and speak german

Font styles to use
Sans Serif

Colors
00a990
33b8a4
9bcb3c
acd036
cadf82
0292cd
3176b5
e34297
e667a6

Requirements
Must have
• Text, which can be edited. It will be in german
• Name of the dental clinic is
• "Velmora - Ihr Zahnarzt in Zug"
Nice to have
• A4 Layout

```html
<!DOCTYPE html>
<html lang="de">
<head>
<meta charset="utf-8">
<title>Velmora – Interdisziplinäre Zahnmedizin</title>
<link href="https://fonts.googleapis.com/css2?family=Barlow:wght@300;400;500;600;700&display=swap" rel="stylesheet">
<style>
  :root{
    --blue:#1172bd;
    --navy:#1b2a5c;
    --pink:#f28b9c;
    --text:#4a4f5c;
    --bg:#e9ecf2;
    --white:#ffffff;
  }
  *{margin:0;padding:0;box-sizing:border-box}
  html,body{width:1200px;height:1200px;overflow:hidden;background:var(--bg);font-family:"Barlow",sans-serif}
  .page{position:absolute;left:168px;top:0;width:864px;height:1200px;background:var(--white);overflow:hidden}
  .title{position:absolute;left:52px;top:80px}
  .title span{display:inline-block;background:var(--blue);color:var(--white);font-weight:500;font-size:70px;line-height:64px;padding:0 2px;letter-spacing:-0.5px;margin-bottom:14px}
  .brand{position:absolute;left:560px;top:80px;width:270px;text-align:center;color:var(--navy)}
  .brand-dot{display:block;width:60px;height:60px;border-radius:50%;background:var(--pink);margin:0 auto 26px}
  .brand-name{font-size:34px;font-weight:400;letter-spacing:8px;line-height:36px}
  .brand-tag{font-size:15px;font-weight:500;line-height:18px;margin-top:6px}
  .subtitle{position:absolute;left:52px;top:252px;color:var(--blue);font-size:28px;font-weight:500;line-height:33px}
  .intro{position:absolute;left:52px;top:406px;width:600px;height:153px;background:var(--pink);color:var(--white);padding:12px 180px 0 22px}
  .intro h2{font-size:22px;font-weight:700;line-height:28px}
  .intro p{font-size:13.5px;font-weight:300;line-height:19px;margin-top:8px}
  .portrait{position:absolute;left:548px;top:286px;width:280px;height:280px;border-radius:50%;border:6px solid var(--pink);background:radial-gradient(circle at 50% 45%,#c9b3a6 0 28%,#a9a9aa 29% 100%)}
  .section{position:absolute;width:371px}
  .section-head{display:flex;align-items:flex-start;height:46px}
  .section-head .marker{width:28px;height:28px;background:var(--pink);display:flex;align-items:center;justify-content:center;margin-right:6px}
  .section-head h3{flex:1;height:100%;background:var(--blue);color:var(--white);font-size:15px;font-weight:700;line-height:17px;padding:5px 9px;letter-spacing:0.2px}
  .section-head.single h3{height:30px;padding-top:6px}
  .section p{font-size:14px;font-weight:300;color:var(--text);line-height:19px;text-align:justify;margin-top:6px;hyphens:auto}
  .rule{position:absolute;left:57px;top:1168px;width:755px;height:6px;background:var(--blue)}
  .footer-band{position:absolute;left:57px;top:1188px;width:755px;height:12px;background:var(--blue)}
</style>
</head>
<body>
<div class="page">
  <h1 class="title"><span>Interdisziplinäre</span><br><span>Zahnmedizin</span></h1>

  <div class="brand">
    <span class="brand-dot"></span>
    <div class="brand-name">VELMORA</div>
    <div class="brand-tag">Ihr Zahnarzt in Zug</div>
  </div>

  <p class="subtitle">Zusammenhang zwischen<br>Zahnproblemen und der<br>Gesundheit von Körper und Geist</p>

  <div class="intro">
    <h2>Zahn und Gesundheit haben<br>eins gemeinsam</h2>
    <p>Man vermisst sie, wenn sie fehlt. Zähne haben einen engen Zusammenhang zur Gesundheit und können diese beeinflussen. Sowohl negativ als auch positiv.</p>
  </div>

  <div class="portrait" role="img" aria-label="Porträtfoto des neuen Zahnarztes"></div>

  <section class="section" style="left:52px;top:625px">
    <div class="section-head"><span class="marker"><svg width="12" height="14" viewBox="0 0 12 14"><path d="M3 2l6 5-6 5" fill="none" stroke="#fff" stroke-width="2.5"/></svg></span><h3>FUNKTION DES KAUORGANS UND INTERDISZIPLINÄRE ZAHNMEDIZIN</h3></div>
    <p>„Funktion ist nicht alles. Aber ohne Funktion ist alles nichts!“ Sagte einst Prof. A. Berthold (Zahnarzt, Gnathologie) und betonte die Bedeutung der Funktion des Kausystems. Sprechen, Kauen aber auch Körperhaltung und Stressmanagement gehören zu den Funktionen der Zähne. Ein gut funktionierendes Kauorgan (nach Prof. R. Lindqvist, interdisziplinäre Zahnmedizin) kann Stress bewältigen und mehr Leistung und Wohlbefinden bringen. Sehr oft erkennt man Funktionsstörungen daran, dass die Zähne nicht richtig zueinander passen oder Muskelverspannungen und Schmerzen im Kiefergelenk auftreten.</p>
  </section>

  <section class="section" style="left:52px;top:916px">
    <div class="section-head"><span class="marker"><svg width="12" height="14" viewBox="0 0 12 14"><path d="M3 2l6 5-6 5" fill="none" stroke="#fff" stroke-width="2.5"/></svg></span><h3>PARODONTITIS UND SYSTEMISCHE ERKRANKUNGEN</h3></div>
    <p>Parodontitis (Entzündung des Zahnhalteapparats) ist eine der häufigsten chronischen Krankheiten weltweit und daher gut erforscht. Herzkrankheiten, Diabetes und Frühgeburtlichkeit sind einige der systemischen Krankheiten mit der Parodontitis in Zusammenhang steht. Zahnfleischbluten, Zahnlockerung, Zahnfleischschwund und Zahnverlust sind typische Begleiterscheinungen von Parodontitis. Eine systematische Parodontitis-Behandlung kann auch positive Auswirkungen auf die gesamte Gesundheit haben.</p>
  </section>

  <section class="section" style="left:441px;top:630px">
    <div class="section-head"><span class="marker"><svg width="12" height="14" viewBox="0 0 12 14"><path d="M3 2l6 5-6 5" fill="none" stroke="#fff" stroke-width="2.5"/></svg></span><h3>ZAHNVERLUST UND NEUROLOGISCHE AUSWIRKUNG</h3></div>
    <p>Ein physiologisches Kausystem hat sehr feine Steuerungs- und Wahrnehmungsmöglichkeiten. Bei Zahnverlust werden diese Fähigkeiten weniger benötigt. Weniger gebrauchte Ressourcen werden von der Natur dementsprechend abgebaut. Studien zeigen, dass Menschen mit weniger Zähnen mehr Risiko zur Bildung von Demenz bergen.</p>
  </section>

  <section class="section" style="left:441px;top:857px">
    <div class="section-head single"><span class="marker"><svg width="12" height="14" viewBox="0 0 12 14"><path d="M3 2l6 5-6 5" fill="none" stroke="#fff" stroke-width="2.5"/></svg></span><h3>GANZHEITLICHE ERKLÄRUNGEN</h3></div>
    <p>Die komplementäre Zahnheilkunde, sehr oft auch als ganzheitliche oder biologische Zahnheilkunde bezeichnet, versucht mit Hilfe von Meridianen (Traditionelle Chinesische Medizin), den Zusammenhang zwischen Zähnen und anderen Organen und Körperteilen zu erklären. Es gibt immer mehr Patienten und Zahnärzte die von dieser Theorie und deren Ergebnissen überzeugt sind. Aufgrund der wissenschaftlichen Lage ist eine ausführliche Aufklärung vor der Behandlung sehr ratsam.</p>
  </section>

  <div class="rule"></div>
  <div class="footer-band"></div>
</div>
</body>
</html>
```